Quillon "5G Sky Mesh Area" Design Kit

Hello Designers!

We are looking for a design kit to advertise the upcoming launch of our "5G Sky Mesh Area". This design kit should be based around an illustrated logo, which will be applied to various media, which shall also include minimal text, using very simple and clean language.

Our kit shall include the following 5 elements:

1. an illustrated logo for our "5G Sky Mesh Area"
2. the "5G Sky Mesh Area" placed on a 'tear drop shaped flag', with relevant contextual design work
3. the "5G Sky Mesh Area" placed on a 'rectangular lamp post sign', with relevant contextual design work
4. the "5G Sky Mesh Area" placed on a rectangular poster shaped design (that will be applied to the 'outside' of a sandwich board) with specific message of "5G Sky Mesh Area - Available Here"
5. the "5G Sky Mesh Area" placed on a rectangular poster shaped design (that will be applied to the 'inside' of a sandwich board) with specific message of "5G Sky Mesh Area - Coming Soon"

Our rollout will be to:
A) place the temporary sandwich board first, announcing that the zone is coming soon
B) flip the sandwich board to announce the zone is "now available"
C) stab the tear drop flags into the ground
D) install the lamp posts signs to state that the zone is present
E) use the illustrated logo on digital media as required

Our CMYK colors include:
-Quillon Green: 50,0,100,0
-Quillon Orange: 0,80,95,0
-Quillon Blue: 70,15,0,0

I've included two design files. The first is our logo, complete with tag line and icons. The second is a sell sheet that was created last year.

Thanks!

Industry/Entity Type

Telecommunications

Font styles to use
Other font styles liked:
• Myriad Pro

Colors

Designer to choose colors to be used in the design.

Requirements
Must have
• Our colors:
• -Quillon Green: 50,0,100,0
• -Quillon Orange: 0,80,95,0
• -Quillon Blue: 70,15,0,0
Should not have
• too much text

```html
<!DOCTYPE html>
<html lang="en">
<head>
<meta charset="utf-8">
<title>Quillon 5G Sky Mesh Area Design Kit</title>
<link rel="stylesheet" href="https://fonts.googleapis.com/css2?family=Exo+2:ital,wght@0,500;0,700;1,800&family=Rajdhani:wght@600&display=swap">
<style>
  :root {
    --navy: #0f3249;
    --orange: #f15a29;
    --sky: #2aa8e0;
    --sky-light: #4fc3f2;
    --green: #8dc63f;
    --white: #ffffff;
    --paper: #ffffff;
  }
  * { box-sizing: border-box; margin: 0; padding: 0; }
  html, body { width: 1200px; height: 1080px; overflow: hidden; background: var(--paper); }
  .kit { position: relative; width: 1200px; height: 1080px; }

  /* Primary lockup */
  .lockup { position: absolute; left: 60px; top: 105px; width: 590px; text-align: center; }
  .lockup-mark { display: block; margin: 0 auto; width: 250px; height: 250px; border-radius: 50%;
    background: linear-gradient(160deg, var(--sky-light) 0%, var(--sky) 45%, var(--navy) 100%); }
  .lockup-name { margin-top: 52px; font-family: "Exo 2", sans-serif; font-weight: 500;
    font-size: 48px; letter-spacing: 5px; color: var(--navy); white-space: nowrap; }

  /* Teardrop flags */
  .flags { position: absolute; left: 0; top: 0; width: 1200px; height: 1080px; }
  .flag-name { font-family: "Exo 2", sans-serif; font-weight: 500; font-size: 17px; fill: var(--sky); }

  /* Sandwich board posters */
  .poster { position: absolute; top: 640px; width: 272px; height: 360px; display: flex; flex-direction: column;
    font-family: "Rajdhani", sans-serif; font-weight: 600; }
  .poster-half { flex: 1; position: relative; }
  .poster-half.navy { background: var(--navy); }
  .poster-half.orange { background: var(--orange); }
  .poster-available { left: 70px; }
  .poster-coming { left: 360px; }
  .poster-message { position: absolute; right: 14px; color: var(--orange); font-size: 44px;
    letter-spacing: 4px; line-height: 52px; text-align: right; }
  .poster-name { position: absolute; left: 0; right: 0; text-align: center; color: var(--navy);
    font-size: 34px; line-height: 40px; white-space: nowrap; transform: scaleX(.86); }
  .poster-mark { position: absolute; left: 50%; width: 52px; height: 52px; margin-left: -26px;
    border-radius: 50%; background: var(--navy); }

  /* Lamp post sign */
  .lamp-sign { position: absolute; left: 824px; top: 642px; width: 256px; height: 358px; }
  .sign-name { font-family: "Exo 2", sans-serif; font-weight: 500; font-size: 19px; fill: var(--sky); }
  .sign-speed { font-family: "Exo 2", sans-serif; font-weight: 800; font-style: italic; font-size: 28px; fill: var(--white); }
  .sign-brand { font-family: "Exo 2", sans-serif; font-weight: 700; font-size: 22px; fill: var(--navy); }
</style>
</head>
<body>
<main class="kit">

  <section class="lockup" aria-label="5G Sky Mesh Area logo">
    <span class="lockup-mark"></span>
    <p class="lockup-name">5G SKY MESH AREA</p>
  </section>

  <svg class="flags" viewBox="0 0 1200 1080" aria-label="Teardrop flags">
    <defs>
      <linearGradient id="flag-rim" x1="0" y1="0" x2="0" y2="1">
        <stop offset="0" stop-color="#4fc3f2"/>
        <stop offset=".35" stop-color="#1d6fa8"/>
        <stop offset="1" stop-color="#0f3249"/>
      </linearGradient>
    </defs>
    <g class="flag flag-left">
      <path d="M931,120 C905,85 860,70 830,72 C795,80 774,130 774,200 C774,300 860,400 931,486 Z" fill="url(#flag-rim)"/>
      <path role="img" aria-label="Circuit-line pattern area" d="M931,150 C900,125 862,115 836,118 C806,126 790,165 790,215 C790,305 865,395 931,470 Z" fill="#0f3249"/>
      <circle cx="866" cy="168" r="20" fill="none" stroke="#2aa8e0" stroke-width="5"/>
      <text class="flag-name" transform="translate(800,212) rotate(64)">5G SKY MESH AREA</text>
    </g>
    <g class="flag flag-right">
      <path d="M972,120 C998,85 1043,70 1073,72 C1108,80 1129,130 1129,200 C1129,300 1043,400 972,486 Z" fill="url(#flag-rim)"/>
      <path role="img" aria-label="Circuit-line pattern area" d="M972,150 C1003,125 1041,115 1067,118 C1097,126 1113,165 1113,215 C1113,305 1038,395 972,470 Z" fill="#0f3249"/>
      <circle cx="1058" cy="168" r="20" fill="none" stroke="#2aa8e0" stroke-width="5"/>
      <text class="flag-name" transform="translate(1100,232) rotate(116) scale(-1,-1)" text-anchor="end">5G SKY MESH AREA</text>
    </g>
  </svg>

  <section class="poster poster-available" aria-label="5G Sky Mesh Area - Available Here">
    <div class="poster-half navy">
      <p class="poster-message" style="top:68px">AVAILABLE<br>HERE</p>
    </div>
    <div class="poster-half orange">
      <p class="poster-name" style="top:2px">5G SKY MESH AREA</p>
      <span class="poster-mark" style="top:48px"></span>
    </div>
  </section>

  <section class="poster poster-coming" aria-label="5G Sky Mesh Area - Coming Soon">
    <div class="poster-half orange">
      <span class="poster-mark" style="top:48px"></span>
      <p class="poster-name" style="top:136px">5G SKY MESH AREA</p>
    </div>
    <div class="poster-half navy">
      <p class="poster-message" style="top:8px">COMING<br>SOON</p>
    </div>
  </section>

  <svg class="lamp-sign" viewBox="0 0 256 358" aria-label="Lamp post sign">
    <rect width="256" height="358" fill="#0f3249"/>
    <circle cx="124" cy="54" r="26" fill="none" stroke="#2aa8e0" stroke-width="6"/>
    <text class="sign-name" transform="translate(36,114) rotate(-6)">5G SKY MESH AREA</text>
    <text class="sign-speed" transform="translate(58,198) rotate(-6)">HIGH SPEED</text>
    <polygon points="0,282 256,222 256,300 0,358" fill="#ffffff"/>
    <circle cx="26" cy="318" r="8" fill="#8dc63f"/>
    <text class="sign-brand" transform="translate(40,326) rotate(-6)">Quillon</text>
  </svg>

</main>
</body>
</html>
```